Stationery Design Project

Need stationery based on logo

Stationery should include:

Letterhead-should include logo at the top, and contact info at the bottom
Envelope should include mailing address  at top left corner (Varrick Study Partners, 4807 Harlow...)
PPT slide should include Logo only
Cover page should just include logo

Requirements
Must have
• Based on logo

```html
<!DOCTYPE html>
<html lang="en">
<head>
<meta charset="utf-8">
<title>Varrick Study Partners – Presentation Template</title>
<link href="https://fonts.googleapis.com/css2?family=Arimo:wght@400;700&display=swap" rel="stylesheet">
<style>
:root{
  --stage:#e4e4e4;
  --stage-light:#f2f2f2;
  --cover:#6b6a63;
  --bar:#7a7a7a;
  --green:#97b92f;
  --ink:#1e1e1e;
  --body-top:#fafafa;
  --body-bottom:#e7e7e7;
  --footer:#ffffff;
  --section:#6e6e6e;
}
*{margin:0;padding:0;box-sizing:border-box}
html,body{width:1200px;height:797px;overflow:hidden}
body{
  font-family:"Arimo",Arial,sans-serif;
  background:radial-gradient(ellipse at 50% 50%,var(--stage-light),var(--stage) 75%);
  position:relative;color:var(--ink);
}
.slide{
  position:absolute;width:378px;height:305px;overflow:hidden;
  box-shadow:2px 3px 6px rgba(0,0,0,.35);
  background:linear-gradient(var(--body-top),var(--body-bottom));
}
.r1{top:65px}.r2{top:428px}
.c1{left:19px}.c2{left:413px}.c3{left:803px}

.slide-cover{background:var(--cover);color:#fff}
.cover-title{position:absolute;left:110px;top:95px;font-size:16px;font-weight:700}
.cover-subtitle{position:absolute;left:110px;top:129px;font-size:11px;font-weight:700}
.cover-brand{position:absolute;left:118px;top:248px;width:150px;text-align:center;
  font-size:17px;letter-spacing:3px;line-height:1.2}
.cover-brand small{display:block;font-size:9px;letter-spacing:2.5px}

.top-bar{position:absolute;left:0;top:0;width:100%;height:19px;background:var(--bar)}
.slide-title{position:absolute;left:13px;top:30px;font-size:13.5px;font-weight:700;color:var(--green)}
.slide-subtitle{position:absolute;left:13px;top:53px;font-size:11px;font-weight:700}
.footer{position:absolute;left:0;bottom:0;width:100%;height:50px;background:var(--footer)}
.footer-contact{position:absolute;left:15px;bottom:11px;font-size:6px;color:var(--green)}
.footer-brand{position:absolute;right:13px;bottom:8px;text-align:center;font-size:9px;
  letter-spacing:1.5px;color:#555;line-height:1.15}
.footer-brand small{display:block;font-size:5.5px;letter-spacing:1px}

.bullets{position:absolute;list-style:none;font-size:10.5px;line-height:1.3}
.bullets li{position:relative;padding-left:9px;margin-bottom:6px}
.bullets li::before{content:"";position:absolute;left:0;top:5px;width:3px;height:3px;background:var(--green)}
.bullets.tight li{margin-bottom:2px}
.bullets.small{font-size:9px;line-height:1.3}
.bullets.small li{margin-bottom:5px}
.bullets.small li::before{top:4px}
.gap{margin-top:16px}

.section-head{position:absolute;left:15px;width:350px;height:15px;background:var(--section);
  color:#fff;font-size:9.5px;font-weight:700;padding:2px 7px;border:1px solid #cfcfcf}

.photo{position:absolute;left:14px;top:81px;width:166px;height:160px;border:2px solid #fff;
  background:linear-gradient(160deg,#dcdcdc 0%,#9b9b9b 45%,#2a2a2a 100%)}
.donut{position:absolute;left:202px;top:80px}

.thanks{position:absolute;left:0;width:100%;top:128px;text-align:center;font-size:19px;color:var(--green)}
.thanks-rule{position:absolute;left:123px;top:173px;width:128px;height:1px;background:#cfcfcf}
</style>
</head>
<body>

<section class="slide slide-cover r1 c1">
  <h1 class="cover-title">Click to add title</h1>
  <p class="cover-subtitle">Click to add subtitle</p>
  <div class="cover-brand">VARRICK<small>STUDY PARTNERS</small></div>
</section>

<section class="slide r1 c2">
  <div class="top-bar"></div>
  <h2 class="slide-title">Enter your title here</h2>
  <p class="slide-subtitle">Enter your subtitle here</p>
  <ul class="bullets" style="left:14px;top:88px">
    <li>This is a dummy text.<br>Please ignore the following content as it is dummy text.</li>
    <li>This is definitely some dummy text.</li>
    <li>The text here is meaningless as it is used to fill this slide.</li>
    <li>Replace this dummy text with our own text.</li>
    <li class="gap">This is definitely some dummy text.</li>
    <li>The text here is meaningless as it is used to fill this slide.</li>
    <li>Replace this dummy text with our own text.</li>
  </ul>
  <div class="footer">
    <span class="footer-contact">hello@varrickstudy.com &nbsp;Page 2</span>
    <div class="footer-brand">VARRICK<small>STUDY PARTNERS</small></div>
  </div>
</section>

<section class="slide r1 c3">
  <div class="top-bar"></div>
  <h2 class="slide-title">Enter your title here</h2>
  <p class="slide-subtitle">Enter your subtitle here</p>
  <div class="section-head" style="top:84px">Enter your title here</div>
  <ul class="bullets tight" style="left:15px;top:104px">
    <li>This is a dummy text.<br>Please ignore the following content as it is dummy text.</li>
    <li>This is definitely some dummy text.</li>
    <li>The text here is meaningless as it is used to fill this slide.</li>
  </ul>
  <div class="section-head" style="top:172px">Enter your title here</div>
  <ul class="bullets tight" style="left:15px;top:191px">
    <li>This is a dummy text.<br>Please ignore the following content as it is dummy text.</li>
    <li>This is definitely some dummy text.</li>
    <li>The text here is meaningless as it is used to fill this slide.</li>
  </ul>
  <div class="footer">
    <span class="footer-contact">hello@varrickstudy.com &nbsp;Page 5</span>
    <div class="footer-brand">VARRICK<small>STUDY PARTNERS</small></div>
  </div>
</section>

<section class="slide r2 c1">
  <div class="top-bar"></div>
  <h2 class="slide-title">Enter your title here</h2>
  <p class="slide-subtitle">Enter your subtitle here</p>
  <ul class="bullets small" style="left:14px;top:88px;width:180px">
    <li>This is a dummy text.<br>Please ignore the following content as it is dummy text.</li>
    <li>This is definitely some dummy text.</li>
    <li>The text here is meaningless as it is used to fill this slide.</li>
    <li>Replace this dummy text with our own text.</li>
  </ul>
  <svg class="donut" width="156" height="156" viewBox="-78 -78 156 156">
    <g stroke="#fff" stroke-width="3">
      <path d="M0,-77 A77,77 0 0 1 66.7,-38.5 L32.9,-19 A38,38 0 0 0 0,-38Z" fill="#d2d2d2"/>
      <path d="M66.7,-38.5 A77,77 0 0 1 66.7,38.5 L32.9,19 A38,38 0 0 0 32.9,-19Z" fill="#ababab"/>
      <path d="M66.7,38.5 A77,77 0 0 1 0,77 L0,38 A38,38 0 0 0 32.9,19Z" fill="#8c8c8c"/>
      <path d="M0,77 A77,77 0 0 1 -66.7,38.5 L-32.9,19 A38,38 0 0 0 0,38Z" fill="#6d6d6d"/>
      <path d="M-66.7,38.5 A77,77 0 0 1 -66.7,-38.5 L-32.9,-19 A38,38 0 0 0 -32.9,19Z" fill="#000"/>
      <path d="M-66.7,-38.5 A77,77 0 0 1 0,-77 L0,-38 A38,38 0 0 0 -32.9,-19Z" fill="#97b92f"/>
    </g>
    <circle r="38" fill="#fff"/>
    <circle r="32" fill="#ececec"/>
    <text y="3.5" text-anchor="middle" font-family="Arimo, Arial, sans-serif" font-size="9.5" font-weight="700" fill="#1e1e1e">Color pallet</text>
  </svg>
  <div class="footer">
    <span class="footer-contact">hello@varrickstudy.com &nbsp;Page 6</span>
    <div class="footer-brand">VARRICK<small>STUDY PARTNERS</small></div>
  </div>
</section>

<section class="slide r2 c2">
  <div class="top-bar"></div>
  <h2 class="slide-title">Enter your title here</h2>
  <p class="slide-subtitle">Enter your subtitle here</p>
  <div class="photo" role="img" aria-label="Black and white photograph of chess pieces on a board"></div>
  <ul class="bullets small" style="left:194px;top:84px;width:172px">
    <li>This is a dummy text.<br>Please ignore the following content as it is dummy text.</li>
    <li>This is definitely some dummy text.</li>
    <li>The text here is meaningless as it is used to fill this slide.</li>
    <li>Replace this dummy text with our own text.</li>
  </ul>
  <div class="footer">
    <span class="footer-contact">hello@varrickstudy.com &nbsp;Page 7</span>
    <div class="footer-brand">VARRICK<small>STUDY PARTNERS</small></div>
  </div>
</section>

<section class="slide r2 c3">
  <div class="top-bar"></div>
  <p class="thanks">Thank you!</p>
  <div class="thanks-rule"></div>
  <div class="footer">
    <span class="footer-contact">hello@varrickstudy.com &nbsp;Page 10</span>
    <div class="footer-brand">VARRICK<small>STUDY PARTNERS</small></div>
  </div>
</section>

</body>
</html>
```